Exciting product design for natural pet treats

We need a design for our stand up doy style pouch that blends well with our current logo and also bold enough to stand out from the crowd.

We have a range of natural, Australian made pet treats and need a generic bag that allows for a sticker to be placed on the bag to idenfity the name, while also allowing a space for another sticker on the back for ingredients.
___
Information for the front is: logo, Australian made and owned, Pet Food Only (this is a small font and should not be hero text), 100% Natural, Visit our web site for more amazing products for your pets, Space for sticker 100 - 150mm x 30mm.
___
Information for the back is: Kibblo Nest is proudly Australian owned and operated. We source all our Kibblo Nest treats from reputable suppliers around Australia.

Our Kibblo Nest treats can be purchased through our online store, where you will find a growing range of other brands and products for your dogs, cats, birds, fish, rabbits, guinea pigs, horses, cows, sheep, chickens and more.

For further information, please visit our web site www.kibblonest.com.au or email us directly info@kibblonest.com.au.
____
The design will be used on three different bag sizes, so our printer can reduce the design from the largest size, but please keep in mind the sizes are 280mm x 380mm, 190mm x 275mm & 160mm x 230mm.

Target Market(s)

Mostly female, 25 to 65 years of age. Pet Lovers, particuarly focussing on dogs.

Industry/Entity Type

pet industry

Requirements
Must have
• Space for sticker on front for the product name 100mm x 30mm. Also a
Nice to have
• Space for a window.
Should not have
• comical pet images. Does not need an image of a pet. Does not need an image of the food.

```html
<!DOCTYPE html>
<html lang="en">
<head>
<meta charset="utf-8">
<title>Kibblo Nest – Treat Pouch Artwork</title>
<link rel="stylesheet" href="https://fonts.googleapis.com/css2?family=Catamaran:wght@400;500;700&family=Open+Sans:ital,wght@1,300&display=swap">
<style>
  :root {
    --purple: #452d6e;
    --teal: #62b5c6;
    --green: #9bc353;
    --cream: #fdf8dc;
    --white: #ffffff;
    --dieline: #29abe2;
    --page: #ffffff;
  }
  * { margin: 0; padding: 0; box-sizing: border-box; }
  html, body {
    width: 1200px; height: 565px; overflow: hidden;
    background: var(--page);
    font-family: "Catamaran", sans-serif;
  }
  .artboard { position: relative; width: 1200px; height: 565px; }
  .panel {
    position: absolute; top: 38px;
    width: 352px; height: 484px;
    outline: 1px solid var(--dieline);
  }
  .panel--front { left: 35px; }
  .panel--back { left: 452px; }
  .panel__art { position: absolute; inset: 0; width: 100%; height: 100%; }

  .brand {
    position: absolute; left: 0; right: 0;
    display: flex; align-items: center; justify-content: center; gap: 8px;
    color: var(--purple); font-weight: 700; line-height: 1;
  }
  .brand__dot { border-radius: 50%; background: var(--teal); flex: none; }
  .panel--front .brand { top: 82px; font-size: 38px; }
  .panel--front .brand__dot { width: 34px; height: 34px; }
  .panel--back .brand { top: 72px; font-size: 26px; }
  .panel--back .brand__dot { width: 24px; height: 24px; }

  .sticker-name {
    position: absolute; left: 113px; top: 212px; width: 126px; height: 38px;
    background: var(--cream);
    display: flex; align-items: center; justify-content: center;
    color: var(--purple); font-size: 14.5px; font-weight: 400;
    font-family: "Catamaran", sans-serif; padding-top: 2px;
  }
  .claim {
    position: absolute; top: 303px;
    font-family: "Open Sans", sans-serif; font-style: italic; font-weight: 300;
    color: var(--white); font-size: 23px; line-height: 1;
  }
  .claim--percent { left: 22px; letter-spacing: 1px; }
  .claim--natural { left: 264px; font-size: 17px; top: 310px; letter-spacing: 4px; }

  .origin {
    position: absolute; left: 0; right: 0; top: 381px;
    text-align: center; color: var(--white);
    font-size: 7px; font-weight: 500; line-height: 9px;
  }
  .tagline {
    position: absolute; left: 0; right: 0; top: 423px;
    text-align: center; color: var(--white);
    font-size: 10px; font-weight: 500;
  }

  .about {
    position: absolute; left: 40px; right: 40px; top: 119px;
    text-align: center; color: var(--white);
    font-size: 9.2px; font-weight: 500; line-height: 10.7px;
  }
  .about p + p { margin-top: 10px; }
  .contact-heading {
    position: absolute; left: 111px; top: 215px; width: 133px; height: 15px;
    background: var(--green); color: var(--white);
    font-size: 9.2px; font-weight: 500;
    display: flex; align-items: center; justify-content: center; padding-top: 1px;
  }
  .contact {
    position: absolute; left: 0; right: 0; top: 230px;
    text-align: center; color: var(--white);
    font-size: 9.2px; font-weight: 500; line-height: 10.6px;
  }
  .ingredients-label {
    position: absolute; left: 50px; top: 292px; width: 254px; height: 99px;
    background: var(--white);
    text-align: center; color: #111; font-family: Arial, sans-serif;
    font-size: 5px; font-weight: 700; padding-top: 6px;
  }
</style>
</head>
<body>
<main class="artboard">

  <section class="panel panel--front" aria-label="Pouch front">
    <svg class="panel__art" viewBox="0 0 751 1032" preserveAspectRatio="none" aria-hidden="true">
      <rect class="body" width="751" height="1032" fill="var(--teal)"/>
      <rect class="top-band" width="751" height="101" fill="var(--purple)"/>
      <line x1="0" y1="68" x2="751" y2="68" stroke="var(--dieline)" stroke-width="1.5"/>
      <line x1="0" y1="80" x2="751" y2="80" stroke="var(--dieline)" stroke-width="1.5" stroke-dasharray="5 4"/>
      <path class="header-rim" d="M0 101 H751 V262 Q376 528 0 262 Z" fill="var(--green)"/>
      <path class="header" d="M0 101 H751 V250 Q376 510 0 250 Z" fill="var(--white)"/>
      <rect class="natural-band" y="638" width="751" height="88" fill="var(--green)"/>
      <ellipse class="window" cx="376" cy="683" rx="161" ry="108" fill="var(--white)"/>
      <rect class="bottom-band" y="883" width="751" height="149" fill="var(--purple)"/>
    </svg>
    <div class="brand"><span class="brand__dot"></span><span class="brand__name">Kibblo Nest</span></div>
    <div class="sticker-name">NAME OF FOOD</div>
    <span class="claim claim--percent">100%</span>
    <span class="claim claim--natural">Natural</span>
    <p class="origin">Australian made and owned<br>Pet Food Only</p>
    <p class="tagline">Visit our web site for more amazing products for your pets</p>
  </section>

  <section class="panel panel--back" aria-label="Pouch back">
    <svg class="panel__art" viewBox="0 0 751 1032" preserveAspectRatio="none" aria-hidden="true">
      <rect class="body" width="751" height="1032" fill="var(--teal)"/>
      <rect class="top-band" width="751" height="101" fill="var(--purple)"/>
      <line x1="0" y1="68" x2="751" y2="68" stroke="var(--dieline)" stroke-width="1.5"/>
      <line x1="0" y1="80" x2="751" y2="80" stroke="var(--dieline)" stroke-width="1.5" stroke-dasharray="5 4"/>
      <rect class="bottom-band" y="883" width="751" height="149" fill="var(--purple)"/>
      <g class="seal-lines" fill="none" stroke="var(--dieline)" stroke-width="1.5" stroke-dasharray="5 4">
        <line x1="27" y1="0" x2="27" y2="1005"/>
        <line x1="725" y1="0" x2="725" y2="1005"/>
        <line x1="27" y1="1005" x2="725" y2="1005"/>
        <path d="M27 895 Q376 1115 725 895"/>
      </g>
    </svg>
    <div class="brand"><span class="brand__dot"></span><span class="brand__name">Kibblo Nest</span></div>
    <div class="about">
      <p>Kibblo Nest is proudly Australian owned and operated. We source all our Kibblo Nest treats from reputable suppliers around Australia.</p>
      <p>Our Kibblo Nest treats can be purchased through our online store, where you will find a growing range of other brands and products for your dogs, cats, birds, fish, rabbits, guinea pigs, horses, cows, sheep, chickens and more.</p>
    </div>
    <div class="contact-heading">For further information,</div>
    <p class="contact">please visit our web site<br>www.kibblonest.com.au<br>or email us directly<br>info@kibblonest.com.au.</p>
    <div class="ingredients-label">Ingredients</div>
  </section>

</main>
</body>
</html>
```